Business Card Design

I would like a new business card design for an accounting firm that specializes in resolving clients tax problems. I want the card to give the impression that we are not your typical stodgy accounting firm, but at the same time we will get the job done.
Industry/Entity Type
Business
Contact Information for Business Card
Dorian T Welsby
Certified Public Accountant
38-27 52nd Street
Sunnyside, NY 11287
Tel: (718) 555-0142
Fax: (888) 555-0199
e-mail: dtwthecpa@ledgerpost.com
website: harborfilingreliefexperts.com

```html
<!DOCTYPE html>
<html lang="en">
<head>
<meta charset="utf-8">
<title>Dorian T Welsby – Business Card</title>
<link href="https://fonts.googleapis.com/css2?family=Marcellus&family=Source+Sans+3:wght@400;600&display=swap" rel="stylesheet">
<style>
  :root {
    --backdrop: #e9e4dc;
    --card-white: #ffffff;
    --blue-light: #0a98dc;
    --blue-deep: #0058ab;
    --violet: #8f5bb0;
    --ink: #111111;
    --muted: #6a6a6a;
    --label-blue: #1587d0;
  }
  html, body {
    margin: 0;
    padding: 0;
    width: 1200px;
    height: 1000px;
    overflow: hidden;
    background: var(--backdrop);
  }
  .canvas {
    position: relative;
    width: 1200px;
    height: 1000px;
  }
  .business-card {
    position: absolute;
    left: 180px;
    top: 260px;
    width: 840px;
    height: 480px;
    background: var(--card-white);
    box-shadow: 0 6px 18px rgba(0,0,0,0.18);
    overflow: hidden;
  }
  .card-art {
    position: absolute;
    inset: 0;
    width: 840px;
    height: 480px;
  }
  .identity {
    position: absolute;
    left: 84px;
    top: 188px;
    color: #ffffff;
  }
  .identity-name {
    font-family: "Marcellus", serif;
    font-size: 38px;
    letter-spacing: 0.5px;
    margin: 0;
    line-height: 1.1;
  }
  .identity-title {
    font-family: "Source Sans 3", sans-serif;
    font-size: 19px;
    margin: 8px 0 0 4px;
    color: #e4f2fb;
  }
  .website {
    position: absolute;
    left: 432px;
    top: 34px;
    font-family: "Source Sans 3", sans-serif;
    font-weight: 600;
    font-size: 17px;
    color: var(--muted);
  }
  .contact {
    position: absolute;
    left: 548px;
    top: 270px;
    font-family: "Source Sans 3", sans-serif;
    font-size: 17px;
    color: var(--ink);
  }
  .address {
    margin: 0 0 16px 0;
    line-height: 1.25;
    font-style: normal;
  }
  .address sup { font-size: 10px; }
  .contact-line {
    display: flex;
    align-items: baseline;
    margin: 0 0 13px 0;
  }
  .contact-label {
    width: 26px;
    color: var(--label-blue);
    font-weight: 600;
  }
</style>
</head>
<body>
<div class="canvas">
  <section class="business-card" aria-label="Business card for Dorian T Welsby, Certified Public Accountant">
    <svg class="card-art" viewBox="0 0 840 480" aria-hidden="true">
      <defs>
        <linearGradient id="panelBlue" x1="0" y1="0" x2="1" y2="0">
          <stop offset="0" stop-color="var(--blue-light)"/>
          <stop offset="1" stop-color="var(--blue-deep)"/>
        </linearGradient>
      </defs>
      <path class="accent-stripe" d="M0 0 H364 L444 200 Q452 220 448 240 L362 480 H0 Z" fill="var(--violet)"/>
      <path class="brand-panel" d="M0 0 H350 L430 200 Q438 220 434 240 L348 480 H0 Z" fill="url(#panelBlue)"/>
    </svg>

    <div class="identity">
      <h1 class="identity-name">Dorian T Welsby</h1>
      <p class="identity-title">Certified Public Accountant</p>
    </div>

    <div class="website">www.harborfilingreliefexperts.com</div>

    <div class="contact">
      <address class="address">38-27 52<sup>nd</sup> Street<br>Sunnyside, NY 11287</address>
      <p class="contact-line"><span class="contact-label">T</span>(718) 555-0142</p>
      <p class="contact-line"><span class="contact-label">F</span>(888) 555-0199</p>
      <p class="contact-line"><span class="contact-label">E</span>dtwthecpa@ledgerpost.com</p>
    </div>
  </section>
</div>
</body>
</html>
```